Label Design for 2x Chutney Products

We need a label design for 2x Chutney Products.
Zintara Chutney - Red Chili
Zintara Chutney - Green Chili & Coriander
See attached pictures. This is just sample pictures so you get an impression of the product and the colors. Both labels to have as title the generic name "Zintara Chutney" and then added either Red Chili or Green Chili & Coriander. The different terms needs to be good readable and can differ in font/color/size, or in the same style if this makes more sense from design point (as I am not a designer). The labels later on need to be editable in the way that the ingredient list, nutrition list, basis company and production information can be added. If this needs to be done directly and cannot be edited later on please let know. Editable design related the additional text also would be good as the additional information need to be added in different languages (Dutch. German and perhaps French). No clue how this is to be implemented but looking forward to receive some input/solutions on this.
I already had a project to create the company logo. I consider this logo to be used as the product logo and not the company logo. A different company logo later on can be designed from new. This logo is here attached. Either to work with this logo and use it as product logo (perhaps revise the colors) and add the product description or create a new logo for the product from scratch if you feel too. The logo itself should be easily readable for the product name/description and the colors appealing to such product and of course customers.
Please contact if any clarification needed. Thanks in advance for your efforts and ideas for this project.

Industry/Entity Type

Food

Other font styles liked:
• Asian Touch

Requirements
Nice to have
• If possible "simply" editable for text fields in order to add/revise the ingredient list, nutrition list, revise to different languages.

```html
<!DOCTYPE html>
<html lang="en">
<head>
<meta charset="utf-8">
<title>Zintara Chutney Labels</title>
<link href="https://fonts.googleapis.com/css2?family=Montserrat:wght@600;700;800&display=swap" rel="stylesheet">
<style>
  :root {
    --bg: #ececec;
    --red: #e8463d;
    --green: #a8c545;
    --green-text: #9bbd3a;
    --ink: #222222;
    --white: #ffffff;
  }
  * { margin: 0; padding: 0; box-sizing: border-box; }
  html, body {
    width: 1200px;
    height: 750px;
    overflow: hidden;
    background: var(--bg);
    font-family: "Montserrat", Arial, sans-serif;
  }
  .canvas {
    position: relative;
    width: 1200px;
    height: 750px;
  }
  .label {
    position: absolute;
    top: 230px;
    width: 276px;
    height: 320px;
    border-radius: 10px;
    overflow: hidden;
    background: var(--white);
  }
  .label--red { left: 255px; --accent: var(--red); --accent-text: var(--red); }
  .label--green { left: 650px; --accent: var(--green); --accent-text: var(--green-text); }

  .label__top-band {
    position: absolute;
    left: 0; top: 0;
    width: 100%;
    height: 100px;
    background: var(--accent);
  }
  .label__bottom-band {
    position: absolute;
    left: 0; bottom: 0;
    width: 100%;
    height: 36px;
    background: var(--accent);
  }
  .brand {
    position: absolute;
    top: 60px;
    left: 0;
    width: 100%;
    display: flex;
    flex-direction: column;
    align-items: center;
  }
  .brand__dot {
    width: 52px;
    height: 52px;
    border-radius: 50%;
    background: var(--white);
  }
  .brand__name {
    margin-top: 6px;
    font-size: 10px;
    font-weight: 700;
    letter-spacing: 1px;
    line-height: 12px;
    color: var(--ink);
    text-align: center;
  }
  .title {
    position: absolute;
    top: 150px;
    left: 0;
    width: 100%;
    text-align: center;
    font-weight: 800;
    line-height: 1;
  }
  .title__name {
    display: block;
    font-size: 28px;
    color: var(--accent-text);
    letter-spacing: 0.5px;
  }
  .title__product {
    display: block;
    margin-top: 4px;
    font-size: 31px;
    color: var(--ink);
  }
  .variant {
    position: absolute;
    top: 218px;
    left: 45px;
    right: 45px;
    display: flex;
    align-items: center;
    gap: 8px;
  }
  .variant__rule {
    flex: 1;
    height: 4px;
    background: var(--accent);
  }
  .variant__text {
    font-size: 20px;
    font-weight: 800;
    color: var(--accent-text);
    text-align: center;
    line-height: 1;
    white-space: nowrap;
  }
  .variant__text--two-line {
    font-size: 13px;
    line-height: 14px;
  }
  .weight {
    position: absolute;
    top: 258px;
    left: 0;
    width: 100%;
    text-align: center;
    font-size: 11px;
    font-weight: 700;
    color: var(--ink);
  }
</style>
</head>
<body>
  <main class="canvas">
    <section class="label label--red">
      <div class="label__top-band"></div>
      <div class="brand">
        <div class="brand__dot"></div>
        <div class="brand__name">KESTREL<br>FOODS</div>
      </div>
      <h1 class="title">
        <span class="title__name">ZINTARA</span>
        <span class="title__product">CHUTNEY</span>
      </h1>
      <div class="variant">
        <span class="variant__rule"></span>
        <span class="variant__text">RED CHILI</span>
        <span class="variant__rule"></span>
      </div>
      <p class="weight">250g</p>
      <div class="label__bottom-band"></div>
    </section>

    <section class="label label--green">
      <div class="label__top-band"></div>
      <div class="brand">
        <div class="brand__dot"></div>
        <div class="brand__name">KESTREL<br>FOODS</div>
      </div>
      <h1 class="title">
        <span class="title__name">ZINTARA</span>
        <span class="title__product">CHUTNEY</span>
      </h1>
      <div class="variant">
        <span class="variant__rule"></span>
        <span class="variant__text variant__text--two-line">GREEN CHILI &amp;<br>CORIANDER</span>
        <span class="variant__rule"></span>
      </div>
      <p class="weight">250g</p>
      <div class="label__bottom-band"></div>
    </section>
  </main>
</body>
</html>
```